Rework of Honey Labels - Updated for clarity

I am looking for a re-do of our current creamed honey labels.
Creamed honey is a butter-consistency. There are 5 flavors - original, lavender, chocolate, lemon, cinnamon. We want for it to look sophisticated and luxurious. We want the labels to all be cohesive in this group, but to be able to easily tell the difference between the products by color or something quick besides just words to tell the difference in the product. The product will be an off-white/light amber - except for the chocolate which is the color of Cremoso. There are three size containers for each of these honeys. But we can just focus on the single size for this contest.
The honey market in our area is extremely competitive. Right now, I feel our labels look more homemade. I want something that stands out. We charge a premium for our products. We want for our labels to look like we are a superior product. We are getting our product in many local stores and need to differentiate ourselves. I am attaching some of the labels that I think stand out. As for the labels themselves. They can include that whole blurb about us as Brookvale Meadow - or not. It is not truly necessary to have on the labels. But the logo needs to be included.
For all of these, we want something unique and special. Like you are going for an English mid-day tea at an upscale hotel in London with the Queen (well, I guess now the King...but really I think of the Queen).
I am uploading our current labels and then a few labels to take inspiration from.
Updates
I just reworked the description to be more limited in what I was asking for. Looking for a label for creamed honey in one size jar only. Thank you.

```html
<!DOCTYPE html>
<html lang="en">
<head>
<meta charset="utf-8">
<title>Creamed Honey Label – Lavender</title>
<link rel="stylesheet" href="https://fonts.googleapis.com/css2?family=Oswald:wght@600&family=Libre+Baskerville&display=swap">
<style>
  :root {
    --bg: #f3f0ea;
    --silver-light: #fbfbfb;
    --silver-mid: #dcdcdc;
    --silver-dark: #a9a9a9;
    --ink: #111111;
    --label-white: #ffffff;
    --brand-green: #3f9a5c;
    --flag-green: #1f5a35;
    --bee-tone: #8a8a8a;
    --dipper-tone: #c9a66b;
  }
  html, body {
    margin: 0;
    width: 1200px;
    height: 1200px;
    overflow: hidden;
    background: var(--bg);
  }
  .canvas {
    position: relative;
    width: 1200px;
    height: 1200px;
  }
  .neck-strip {
    position: absolute;
    left: 535px;
    top: 30px;
    width: 130px;
    height: 270px;
  }
  .main-label {
    position: absolute;
    left: 360px;
    top: 330px;
    width: 480px;
    height: 800px;
  }
  .serif { font-family: "Libre Baskerville", Georgia, serif; }
  .condensed { font-family: "Oswald", "Arial Narrow", sans-serif; font-weight: 600; }
</style>
</head>
<body>
<main class="canvas">

  <svg class="neck-strip" viewBox="0 0 130 270" aria-label="Neck strip: Creamed Honey">
    <defs>
      <linearGradient id="stripSilver" x1="0" x2="1" y1="0" y2="0">
        <stop offset="0" stop-color="var(--silver-dark)"/>
        <stop offset="0.5" stop-color="var(--silver-light)"/>
        <stop offset="1" stop-color="var(--silver-mid)"/>
      </linearGradient>
    </defs>
    <rect x="0" y="0" width="130" height="270" fill="url(#stripSilver)"/>
    <rect x="18" y="0" width="94" height="252" fill="var(--label-white)" stroke="var(--ink)" stroke-width="2.5"/>
    <text class="condensed" x="65" y="126" fill="var(--ink)" font-size="34" text-anchor="middle" dominant-baseline="middle" transform="rotate(90 65 126)">CREAMED HONEY</text>
  </svg>

  <svg class="main-label" viewBox="0 0 480 800" aria-label="Lavender creamed honey label">
    <defs>
      <linearGradient id="labelSilver" x1="0" x2="1" y1="0" y2="0">
        <stop offset="0" stop-color="var(--silver-dark)"/>
        <stop offset="0.35" stop-color="var(--silver-light)"/>
        <stop offset="0.7" stop-color="var(--silver-mid)"/>
        <stop offset="1" stop-color="var(--silver-dark)"/>
      </linearGradient>
      <path id="arcPath" d="M 35 262 A 205 205 0 0 1 445 262"/>
    </defs>

    <rect class="outer-frame" x="2" y="2" width="476" height="796" rx="238" fill="url(#labelSilver)" stroke="var(--ink)" stroke-width="2"/>

    <rect class="inner-panel" x="50" y="72" width="380" height="700" rx="190" fill="var(--label-white)" stroke="var(--ink)" stroke-width="3"/>

    <text class="serif arc-tagline" fill="var(--ink)" font-size="21" letter-spacing="1.5">
      <textPath href="#arcPath" startOffset="50%" text-anchor="middle">HOMEMADE PREMIUM QUALITY</textPath>
    </text>

    <rect role="img" aria-label="Bee illustration framed by lavender sprigs" x="150" y="100" width="180" height="122" rx="10" fill="var(--bee-tone)" opacity="0.35"/>

    <rect role="img" aria-label="Honey dipper" x="80" y="232" width="150" height="14" rx="7" fill="var(--dipper-tone)"/>
    <rect role="img" aria-label="Honey dipper" x="250" y="232" width="150" height="14" rx="7" fill="var(--dipper-tone)"/>

    <text class="condensed product-title" x="240" y="310" fill="var(--ink)" font-size="50" text-anchor="middle">CREAMED HONEY</text>

    <text class="serif brand-name" x="240" y="420" fill="var(--brand-green)" font-size="36" text-anchor="middle">Brookvale</text>
    <text class="serif brand-name" x="240" y="468" fill="var(--brand-green)" font-size="36" text-anchor="middle">Meadow</text>

    <rect role="img" aria-label="Green flag ornament" x="62" y="548" width="30" height="26" fill="var(--flag-green)"/>
    <rect role="img" aria-label="Green flag ornament" x="388" y="548" width="30" height="26" fill="var(--flag-green)"/>
    <text class="serif flavor-name" x="240" y="573" fill="var(--ink)" font-size="32" text-anchor="middle">LAVENDER</text>

    <text class="serif" x="240" y="622" fill="var(--ink)" font-size="19" text-anchor="middle">100% NATURAL</text>
    <text class="serif" x="240" y="652" fill="var(--ink)" font-size="19" text-anchor="middle">PRODUCT</text>

    <rect role="img" aria-label="Honey dipper" x="80" y="680" width="150" height="14" rx="7" fill="var(--dipper-tone)"/>
    <rect role="img" aria-label="Honey dipper" x="250" y="680" width="150" height="14" rx="7" fill="var(--dipper-tone)"/>
  </svg>

</main>
</body>
</html>
```